Eye Catching Business Card for Optometrist

We've recently refreshed our logo and now we need a fresh and bold look for our business cards. We provide progressive ways to improve people's vision and protect their eye health.

Use our new logo as guidance into the colors to use. As far as style goes, I love how bold and eye catching the card is for Lantern Works. Feel free to use your creative judgement.

Tagline: "Clearly the best for your vision."

pertinent info to include:

Dr. Martin Pruell
Optometrist

2857 Wilmarth Ridge Blvd #207
Harlow Springs, MO 64120
(555) 382-9017

marty@brindlecoveeyecare.example
www.brindlecoveeyecare.example

```html
<!DOCTYPE html>
<html lang="en">
<head>
<meta charset="utf-8">
<title>Brindle Cove Eye Care – Business Card</title>
<link href="https://fonts.googleapis.com/css2?family=Open+Sans:wght@300;400;700&family=Josefin+Sans:wght@700&family=Arimo:wght@400&display=swap" rel="stylesheet">
<style>
  :root {
    --brand-red: #a3152a;
    --ink: #4a4440;
    --tagline-grey: #7d7f82;
    --paper-light: #fbdfae;
    --paper-mid: #f6cf94;
    --paper-edge: #eebd80;
    --frame: #555555;
    --page: #ffffff;
  }
  * { margin: 0; padding: 0; box-sizing: border-box; }
  html, body { width: 1200px; height: 1000px; overflow: hidden; background: var(--page); }
  .presentation {
    position: relative;
    width: 1200px;
    height: 1000px;
    border: 1px solid var(--frame);
    background: var(--page);
    overflow: hidden;
  }
  .accent-bar { position: absolute; background: var(--brand-red); }
  .accent-bar--top-right { left: 1169px; top: 0; width: 31px; height: 186px; }
  .accent-bar--bottom-left { left: 0; top: 818px; width: 32px; height: 182px; }

  .card {
    position: absolute;
    left: 258px;
    width: 686px;
    height: 416px;
    background: radial-gradient(ellipse at 50% 45%, var(--paper-light) 0%, var(--paper-mid) 60%, var(--paper-edge) 100%);
  }
  .card--front { top: 60px; }
  .card--back { top: 525px; }

  .brand {
    position: absolute;
    left: 0; right: 0; top: 108px;
    text-align: center;
  }
  .brand__mark {
    display: block;
    width: 84px; height: 84px;
    margin: 0 auto 26px;
    background: var(--brand-red);
  }
  .brand__name {
    font-family: "Open Sans", sans-serif;
    font-weight: 700;
    font-size: 36px;
    line-height: 40px;
    color: var(--brand-red);
    letter-spacing: 1px;
    text-transform: uppercase;
  }
  .tagline {
    position: absolute;
    left: 0; right: 0; top: 328px;
    text-align: center;
    font-family: "Open Sans", sans-serif;
    font-weight: 300;
    font-size: 27px;
    color: var(--tagline-grey);
  }

  .person {
    position: absolute;
    left: 0; right: 0; top: 40px;
    text-align: center;
  }
  .person__name {
    font-family: "Josefin Sans", sans-serif;
    font-weight: 700;
    font-size: 42px;
    letter-spacing: 1.5px;
    color: var(--brand-red);
    text-transform: uppercase;
    line-height: 48px;
  }
  .person__role {
    font-family: "Arimo", sans-serif;
    font-size: 29px;
    color: var(--ink);
    margin-top: 2px;
  }

  .contact {
    position: absolute;
    left: 142px; top: 218px;
    list-style: none;
    font-family: "Arimo", sans-serif;
    font-size: 21.5px;
    color: var(--ink);
  }
  .contact__item {
    display: flex;
    align-items: flex-start;
    height: 40.5px;
  }
  .contact__icon {
    width: 26px; height: 26px;
    margin-right: 26px;
    flex: none;
    fill: none;
    stroke: var(--brand-red);
    stroke-width: 1.6;
  }
  .contact__text { line-height: 26px; }
</style>
</head>
<body>
<div class="presentation">
  <div class="accent-bar accent-bar--top-right"></div>
  <div class="accent-bar accent-bar--bottom-left"></div>

  <section class="card card--front">
    <div class="brand">
      <span class="brand__mark"></span>
      <div class="brand__name">Brindle Cove<br>Eye Care</div>
    </div>
    <p class="tagline">Clearly the best for your vision</p>
  </section>

  <section class="card card--back">
    <div class="person">
      <h1 class="person__name">Dr. Martin Pruell</h1>
      <p class="person__role">Optometrist</p>
    </div>
    <ul class="contact">
      <li class="contact__item">
        <svg class="contact__icon" viewBox="0 0 26 26" aria-hidden="true"><path d="M8 3 L11 8 L9 10 Q10 14 14 17 L16 15 L21 18 L19 22 Q9 21 5 7 Z" style="fill:var(--brand-red);stroke:none"/></svg>
        <span class="contact__text">(555) 382-9017</span>
      </li>
      <li class="contact__item">
        <svg class="contact__icon" viewBox="0 0 26 26" aria-hidden="true"><circle cx="13" cy="13" r="10"/><ellipse cx="13" cy="13" rx="4.5" ry="10"/><line x1="3" y1="13" x2="23" y2="13"/><path d="M5 7.5 H21 M5 18.5 H21"/></svg>
        <span class="contact__text">www.brindlecoveeyecare.example</span>
      </li>
      <li class="contact__item">
        <svg class="contact__icon" viewBox="0 0 26 26" aria-hidden="true"><rect x="2" y="6" width="22" height="14"/><path d="M2 6 L13 15 L24 6 M2 20 L10 12.5 M24 20 L16 12.5"/></svg>
        <span class="contact__text">marty@brindlecoveeyecare.example</span>
      </li>
      <li class="contact__item">
        <svg class="contact__icon" viewBox="0 0 26 26" aria-hidden="true"><path d="M13 25 L6 13 A8 8 0 1 1 20 13 Z" style="fill:var(--brand-red);stroke:none"/><circle cx="13" cy="9" r="3" style="fill:var(--paper-mid);stroke:none"/></svg>
        <span class="contact__text">2857 Wilmarth Ridge Blvd #207<br>Harlow Springs, MO 64120</span>
      </li>
    </ul>
  </section>
</div>
</body>
</html>
```